AI Business Tools Landing Page

My web-based website builder (Brindora.com) will be adding many new features in the very near future and I need an eye-catching landing page to promote these new products.

The page will have a primary section of the 8 main products we are promoting:
1. AI Instant Website Generator
2. AI Chatbot
3. Online Store Builder with AI Assistance
4. AI Auto-Blogging System
5. Online Scheduling System
6. Custom Email System
7. SEO Service
8. CRM System

The page will also have a smaller section for links to our affiliate programs. These can be smaller, less-promanent buttons or links. These are the affiliate products:
1. Get Your LLC
2. Website Design and Maintenance
3. Vorlo Ads Management
4. Social Media Posting Service
5. Logo Design
6. Trademark Registration
7. Patent Application
8. Printing Services (including postcards, flyers, and merch.)
9. Bulk AI Content Generator

The theme and color scheme of the page should follow the theme of our main website, which is https://brindora.com.

I need the page fully coded and ready to deploy on my server.

I look forward to seeing your amazing designs!

```html
<!DOCTYPE html>
<html lang="en">
<head>
<meta charset="UTF-8">
<title>Brindora – AI Business Tools</title>
<link rel="stylesheet" href="https://fonts.googleapis.com/css2?family=Poppins:wght@400;500;600;700;800&display=swap">
<style>
  :root{
    --navy:#0a0a3c;
    --blue:#1e7fe0;
    --card:#e6e7ec;
    --ink:#0d0d2e;
    --muted:#5a5d6e;
    --line:#c9ccd8;
    --white:#ffffff;
  }
  *{margin:0;padding:0;box-sizing:border-box}
  html,body{width:1200px;height:2588px;overflow:hidden}
  body{font-family:'Poppins',sans-serif;background:var(--white);color:var(--ink);position:relative}

  .site-header{position:absolute;top:0;left:0;width:1200px;height:250px}
  .site-header svg{position:absolute;inset:0}
  .brand{position:absolute;top:46px;left:0;width:1200px;display:flex;justify-content:center;align-items:center;gap:14px}
  .brand-mark{width:42px;height:42px;border-radius:50%;background:var(--blue)}
  .brand-name{font-size:40px;font-weight:700;color:var(--white);letter-spacing:.5px}

  .tools{position:absolute;top:290px;left:0;width:1200px;height:1390px}
  .tools svg.band{position:absolute;inset:0}
  .tools-title{position:absolute;top:115px;left:112px;font-size:40px;font-weight:700;color:var(--white)}
  .tool-grid{position:absolute;top:230px;left:112px;display:grid;grid-template-columns:repeat(3,308px);column-gap:24px;row-gap:40px}
  .tool-card{background:var(--card);height:320px;padding:28px 18px;display:flex;flex-direction:column;align-items:center;text-align:center}
  .tool-icon{width:84px;height:84px;border-radius:50%;background:var(--white);border:3px solid var(--navy);display:flex;align-items:center;justify-content:center;flex-shrink:0}
  .tool-name{margin-top:18px;font-size:19px;font-weight:700;line-height:1.3;color:var(--ink);white-space:nowrap}
  .tool-text{margin-top:12px;font-size:12px;line-height:1.55;color:var(--muted);padding:0 8px}

  .affiliates{position:absolute;top:1760px;left:0;width:1200px}
  .section-title{font-size:32px;font-weight:700;text-align:center;color:var(--ink)}
  .affiliate-list{list-style:none;display:grid;grid-template-columns:repeat(3,308px);column-gap:24px;row-gap:22px;margin:44px 0 0 112px}
  .affiliate-link{display:flex;align-items:center;justify-content:space-between;gap:12px;height:74px;padding:0 22px;border:1.5px solid var(--line);border-radius:10px;background:var(--white);font-size:16px;font-weight:500;line-height:1.3;color:var(--ink);text-decoration:none}
  .affiliate-link svg{flex-shrink:0}

  .site-footer{position:absolute;top:2400px;left:0;width:1200px;height:188px}
  .site-footer svg.edge{position:absolute;top:0;left:0}
  .copyright{position:absolute;top:98px;left:100px;font-size:15px;font-weight:500}
  .footer-brand{position:absolute;top:86px;left:0;width:1200px;display:flex;justify-content:center;align-items:center;gap:12px}
  .footer-brand .brand-mark{width:36px;height:36px}
  .footer-brand .brand-name{font-size:34px;color:var(--navy)}
  .social{position:absolute;top:98px;right:100px;display:flex;gap:10px}
  .social span{width:20px;height:20px;border-radius:50%;background:var(--navy)}
</style>
</head>
<body>

<header class="site-header">
  <svg width="1200" height="250" viewBox="0 0 1200 250" aria-hidden="true">
    <path d="M0 0H1200V150C1000 235 820 225 600 195C380 165 200 185 0 230Z" fill="var(--navy)"/>
    <path d="M560 232C800 250 980 220 1200 150" fill="none" stroke="var(--blue)" stroke-width="14"/>
  </svg>
  <div class="brand"><span class="brand-mark"></span><span class="brand-name">Brindora</span></div>
</header>

<section class="tools">
  <svg class="band" width="1200" height="1390" viewBox="0 0 1200 1390" aria-hidden="true">
    <path d="M0 60C300 0 600 20 900 45C1020 55 1120 40 1200 20V1350C900 1400 400 1380 0 1360Z" fill="var(--navy)"/>
    <path d="M0 42C260 -5 520 10 760 30" fill="none" stroke="var(--blue)" stroke-width="10"/>
  </svg>
  <h2 class="tools-title">More Tools to Help Your Grow Your Business</h2>
  <div class="tool-grid">
    <article class="tool-card">
      <div class="tool-icon"><svg width="44" height="44" viewBox="0 0 44 44" fill="none" stroke="var(--navy)" stroke-width="3"><rect x="5" y="8" width="34" height="24" rx="2"/><path d="M16 38h12M22 32v6"/></svg></div>
      <h3 class="tool-name">AI Instant<br>Website Generator</h3>
      <p class="tool-text">Get a professional, fully optimized website in seconds. Includes custom domain, secure hosting and mobile-ready layouts.</p>
    </article>
    <article class="tool-card">
      <div class="tool-icon"><svg width="44" height="44" viewBox="0 0 44 44" fill="none" stroke="var(--navy)" stroke-width="3"><path d="M6 8h32v22H18l-8 7v-7H6z"/></svg></div>
      <h3 class="tool-name">AI ChatBot</h3>
      <p class="tool-text">Fully trainable chatbot that learns about your business to answer visitor questions around the clock. Built-in CRM saves leads automatically.</p>
    </article>
    <article class="tool-card">
      <div class="tool-icon"><svg width="44" height="44" viewBox="0 0 44 44" fill="none" stroke="var(--navy)" stroke-width="3"><path d="M4 8h6l5 20h20l4-14H13"/><circle cx="17" cy="35" r="3"/><circle cx="32" cy="35" r="3"/></svg></div>
      <h3 class="tool-name">Online Store Builder<br>(E-Commerce)<br>with AI Assistance</h3>
      <p class="tool-text">Add products online and let our assistant write descriptions for you. Accept payments through many popular gateways.</p>
    </article>
    <article class="tool-card">
      <div class="tool-icon"><svg width="44" height="44" viewBox="0 0 44 44" fill="none" stroke="var(--navy)" stroke-width="3"><path d="M10 4h18l8 8v28H10z"/><path d="M16 20h14M16 27h14M16 34h9"/></svg></div>
      <h3 class="tool-name">AI Auto-Blogging<br>System</h3>
      <p class="tool-text">A self-managing blog that researches, writes and publishes fresh articles for your site. Keep your content growing every week.</p>
    </article>
    <article class="tool-card">
      <div class="tool-icon"><svg width="44" height="44" viewBox="0 0 44 44" fill="none" stroke="var(--navy)" stroke-width="3"><rect x="5" y="8" width="34" height="30" rx="2"/><path d="M5 17h34M14 4v8M30 4v8"/></svg></div>
      <h3 class="tool-name">Online Scheduling<br>System</h3>
      <p class="tool-text">Set appointment settings, reminders and availability. Customers book the right time from your site and everything syncs to one dashboard.</p>
    </article>
    <article class="tool-card">
      <div class="tool-icon"><svg width="44" height="44" viewBox="0 0 44 44" fill="none" stroke="var(--navy)" stroke-width="3"><rect x="5" y="10" width="34" height="24" rx="2"/><path d="M5 12l17 12 17-12"/></svg></div>
      <h3 class="tool-name">Custom emails using<br>your domain</h3>
      <p class="tool-text">Quickly set up branded emails for yourself and your team. Send and receive from any device and manage every inbox in one place.</p>
    </article>
    <article class="tool-card">
      <div class="tool-icon"><svg width="44" height="44" viewBox="0 0 44 44" fill="none" stroke="var(--navy)" stroke-width="3"><circle cx="19" cy="19" r="12"/><path d="M28 28l11 11"/></svg></div>
      <h3 class="tool-name">SEO Service –<br>Automatic Backlink Building</h3>
      <p class="tool-text">Let us do the hard work of earning quality backlinks to your website. Climb higher in search results without extra effort.</p>
    </article>
    <article class="tool-card">
      <div class="tool-icon"><svg width="44" height="44" viewBox="0 0 44 44" fill="none" stroke="var(--navy)" stroke-width="3"><circle cx="22" cy="15" r="7"/><path d="M8 39c0-8 6-13 14-13s14 5 14 13"/></svg></div>
      <h3 class="tool-name">Customer Relationship<br>Management (CRM) System</h3>
      <p class="tool-text">Automate the lead follow-up process to connect with every contact. Schedule email and text campaigns and keep customers coming back.</p>
    </article>
  </div>
</section>

<section class="affiliates">
  <h2 class="section-title">Additional Features for Your Website</h2>
  <ul class="affiliate-list">
    <li><a class="affiliate-link" href="#">Get Your LLC<svg width="18" height="18" viewBox="0 0 18 18" fill="none" stroke="var(--blue)" stroke-width="2.4"><path d="M3 9h11M10 4l5 5-5 5"/></svg></a></li>
    <li><a class="affiliate-link" href="#">Website Design and Maintenance<svg width="18" height="18" viewBox="0 0 18 18" fill="none" stroke="var(--blue)" stroke-width="2.4"><path d="M3 9h11M10 4l5 5-5 5"/></svg></a></li>
    <li><a class="affiliate-link" href="#">Vorlo Ads Management<svg width="18" height="18" viewBox="0 0 18 18" fill="none" stroke="var(--blue)" stroke-width="2.4"><path d="M3 9h11M10 4l5 5-5 5"/></svg></a></li>
    <li><a class="affiliate-link" href="#">Social Media Posting Service<svg width="18" height="18" viewBox="0 0 18 18" fill="none" stroke="var(--blue)" stroke-width="2.4"><path d="M3 9h11M10 4l5 5-5 5"/></svg></a></li>
    <li><a class="affiliate-link" href="#">Logo Design<svg width="18" height="18" viewBox="0 0 18 18" fill="none" stroke="var(--blue)" stroke-width="2.4"><path d="M3 9h11M10 4l5 5-5 5"/></svg></a></li>
    <li><a class="affiliate-link" href="#">Trademark Registration<svg width="18" height="18" viewBox="0 0 18 18" fill="none" stroke="var(--blue)" stroke-width="2.4"><path d="M3 9h11M10 4l5 5-5 5"/></svg></a></li>
    <li><a class="affiliate-link" href="#">Patent Application<svg width="18" height="18" viewBox="0 0 18 18" fill="none" stroke="var(--blue)" stroke-width="2.4"><path d="M3 9h11M10 4l5 5-5 5"/></svg></a></li>
    <li><a class="affiliate-link" href="#">Printing Services (including postcards, flyers, and merch.)<svg width="18" height="18" viewBox="0 0 18 18" fill="none" stroke="var(--blue)" stroke-width="2.4"><path d="M3 9h11M10 4l5 5-5 5"/></svg></a></li>
    <li><a class="affiliate-link" href="#">Bulk AI Content Generator<svg width="18" height="18" viewBox="0 0 18 18" fill="none" stroke="var(--blue)" stroke-width="2.4"><path d="M3 9h11M10 4l5 5-5 5"/></svg></a></li>
  </ul>
</section>

<footer class="site-footer">
  <svg class="edge" width="1200" height="80" viewBox="0 0 1200 80" aria-hidden="true">
    <path d="M0 0H1200V10C900 70 500 60 0 30Z" fill="var(--navy)"/>
    <path d="M0 34C400 62 800 70 1200 14" fill="none" stroke="var(--blue)" stroke-width="8"/>
  </svg>
  <p class="copyright">© 2024 Brindora. All Rights Reserved</p>
  <div class="footer-brand"><span class="brand-mark"></span><span class="brand-name">Brindora</span></div>
  <nav class="social" aria-label="Social links">
    <span></span><span></span><span></span><span></span><span></span><span></span><span></span><span></span>
  </nav>
</footer>

</body>
</html>
```